Stationary Design for Norvath Digital

We are after a full stationary back business cards, letterheads, compliment slip, invoice template, delivery note and anything else we could use within the stationary pack.

We would also like an email footer creating.

Our company details to be included on all stationary:

Registered Name: Norvath Limited
Company Registration Number: 20473915
Website: www.norvathdigital.example
email: info@norvathdigital.example
Phone: 01632 960 417
Address: 48 Tamsin Lane Loughborough Leicestershire United Kingdom LE11 9QX

```html
<!DOCTYPE html>
<html lang="en">
<head>
<meta charset="utf-8">
<title>Norvath Digital Letterhead</title>
<link rel="stylesheet" href="https://fonts.googleapis.com/css2?family=Questrial&display=swap">
<style>
  :root {
    --purple-deep: #3b2453;
    --plum: #6a2544;
    --red: #d9322c;
    --red-bright: #e43c33;
    --footer-dark: #2b2023;
    --footer-red: #c3241f;
    --stripe-yellow: #d8c71c;
    --stripe-olive: #8d8416;
    --paper: #ffffff;
    --ink-light: #ffffff;
  }
  html, body {
    margin: 0;
    padding: 0;
    overflow: hidden;
    background: var(--paper);
  }
  .letterhead {
    position: relative;
    width: 927px;
    height: 1200px;
    background: var(--paper);
    overflow: hidden;
    font-family: "Questrial", sans-serif;
    color: var(--ink-light);
  }
  .header-band {
    position: absolute;
    left: 0; top: 0;
    width: 927px; height: 170px;
    background:
      radial-gradient(circle at 560px 40px, rgba(255,255,255,0.12), transparent 140px),
      radial-gradient(circle at 720px 90px, rgba(255,180,160,0.12), transparent 90px),
      linear-gradient(90deg, var(--purple-deep) 0%, var(--plum) 35%, var(--red) 75%, var(--red-bright) 100%);
  }
  .accent-stripe {
    position: absolute;
    top: 106px;
    height: 10px;
    background: linear-gradient(180deg, var(--stripe-olive) 0%, var(--stripe-yellow) 35%, var(--stripe-yellow) 65%, var(--stripe-olive) 100%);
  }
  .accent-stripe--left { left: 0; width: 60px; }
  .accent-stripe--right { left: 270px; right: 0; }
  .brand-name {
    position: absolute;
    left: 62px;
    top: 88px;
    width: 200px;
    font-size: 38px;
    line-height: 46px;
    letter-spacing: 1px;
    color: var(--ink-light);
    white-space: nowrap;
  }
  .footer-band {
    position: absolute;
    left: 0; top: 1064px;
    width: 927px; height: 136px;
    background:
      radial-gradient(circle at 820px 110px, rgba(255,255,255,0.10), transparent 90px),
      radial-gradient(circle at 560px 20px, rgba(255,255,255,0.08), transparent 80px),
      linear-gradient(90deg, var(--footer-dark) 0%, #4a2428 40%, #9e2420 75%, var(--footer-red) 100%);
  }
  .footer-address, .footer-contact {
    position: absolute;
    margin: 0;
    font-size: 12.5px;
    line-height: 14px;
    font-style: normal;
  }
  .footer-address { left: 37px; top: 1136px; }
  .footer-contact { left: 705px; top: 1126px; font-size: 12px; line-height: 13px; }
  .footer-company {
    position: absolute;
    left: 385px;
    top: 1106px;
    text-align: left;
  }
  .company-name {
    margin: 0;
    font-size: 27px;
    line-height: 30px;
    font-weight: normal;
  }
  .company-reg {
    margin: 0;
    font-size: 12.5px;
    line-height: 14px;
  }
</style>
</head>
<body>
  <main class="letterhead">
    <div class="header-band" role="img" aria-label="Purple to red gradient header with soft bokeh light texture"></div>
    <div class="accent-stripe accent-stripe--left"></div>
    <div class="accent-stripe accent-stripe--right"></div>
    <div class="brand-name">Norvath</div>

    <div class="footer-band" role="img" aria-label="Dark to red gradient footer with soft bokeh light texture"></div>
    <address class="footer-address">
      48 Tamsin Lane Loughborough<br>
      Leicestershire United Kingdom, LE11 9QX
    </address>
    <div class="footer-company">
      <p class="company-name">Norvath Limited</p>
      <p class="company-reg">Company Reg #: 20473915</p>
    </div>
    <p class="footer-contact">
      phone: 01632 960 417<br>
      email: info@norvathdigital.example<br>
      website: www.norvathdigital.example
    </p>
  </main>
</body>
</html>
```